Lumora Business Card Design

hello,
we are looking for a business card design for our Fintech Company. We are credit card processing company that is also expanding in to the crypto market. We will be focusing on crypto processing, with a crypto wallet and crypto exchange. We like the purple in the logo. We want something modern and sophisticated but at the same time simple and trust worthy to work with banks.

Industry/Entity Type

Fintech

Logo Text

Lumora

```html
<!DOCTYPE html>
<html lang="en">
<head>
<meta charset="utf-8">
<title>Lumora Business Card</title>
<link rel="stylesheet" href="https://fonts.googleapis.com/css2?family=Roboto:wght@400;500;700;900&display=swap">
<style>
  :root {
    --backdrop: #b1b0ae;
    --card: #ffffff;
    --navy: #24355b;
    --violet: #5449a0;
    --ink: #1a1a1a;
  }
  * { margin: 0; padding: 0; box-sizing: border-box; }
  html, body {
    width: 1200px;
    height: 1200px;
    overflow: hidden;
    background: var(--backdrop);
    font-family: "Roboto", sans-serif;
  }
  .card {
    position: absolute;
    left: 229px;
    width: 745px;
    height: 418px;
    background: var(--card);
  }
  .card--front { top: 163px; }
  .card--back { top: 620px; display: flex; align-items: center; justify-content: center; }

  .wordmark {
    font-family: "Roboto", sans-serif;
    font-weight: 700;
    color: var(--violet);
    letter-spacing: -0.04em;
    line-height: 1;
  }
  .card--front .wordmark {
    position: absolute;
    left: 24px;
    top: 4px;
    font-size: 146px;
  }
  .card--back .wordmark {
    font-size: 178px;
    margin-top: 6px;
  }

  .person { position: absolute; left: 26px; top: 214px; }
  .person__name {
    font-weight: 700;
    font-size: 27px;
    color: var(--violet);
    letter-spacing: 0.01em;
    line-height: 1.1;
  }
  .person__role {
    font-weight: 400;
    font-size: 18px;
    color: var(--ink);
    margin-top: 2px;
  }

  .divider {
    position: absolute;
    left: 26px;
    width: 692px;
    top: 292px;
    height: 2px;
    background: var(--violet);
  }

  .contact {
    position: absolute;
    left: 26px;
    top: 316px;
    list-style: none;
  }
  .contact__item {
    display: flex;
    align-items: center;
    height: 27.5px;
    font-size: 18.5px;
    color: var(--ink);
  }
  .contact__icon {
    width: 17px;
    height: 17px;
    margin-right: 2px;
    fill: var(--violet);
    flex: none;
  }

  .address {
    position: absolute;
    right: 27px;
    top: 340px;
    text-align: right;
    font-style: normal;
    font-size: 18.5px;
    line-height: 27.5px;
    color: var(--ink);
  }
</style>
</head>
<body>
  <section class="card card--front">
    <div class="wordmark">Lumora</div>

    <div class="person">
      <div class="person__name">MAREN COLE</div>
      <div class="person__role">Founder/CEO</div>
    </div>

    <div class="divider"></div>

    <ul class="contact">
      <li class="contact__item">
        <svg class="contact__icon" viewBox="0 0 24 24" aria-hidden="true">
          <path d="M6.6 10.8a15.1 15.1 0 0 0 6.6 6.6l2.2-2.2c.3-.3.7-.4 1-.2 1.1.4 2.3.6 3.6.6.6 0 1 .4 1 1V20c0 .6-.4 1-1 1A17 17 0 0 1 3 4c0-.6.4-1 1-1h3.5c.6 0 1 .4 1 1 0 1.3.2 2.5.6 3.6.1.3 0 .7-.2 1l-2.3 2.2z"/>
        </svg>
        <span>555-0142-00</span>
      </li>
      <li class="contact__item">
        <svg class="contact__icon" viewBox="0 0 24 24" aria-hidden="true">
          <path d="M2 6h20v12H2z M2 6l10 7 10-7" fill="var(--violet)"/>
          <path d="M2.5 6.5l9.5 6.6 9.5-6.6" fill="none" stroke="#fff" stroke-width="1.4"/>
        </svg>
        <span>info@lumorapay.com</span>
      </li>
      <li class="contact__item">
        <svg class="contact__icon" viewBox="0 0 24 24" aria-hidden="true">
          <circle cx="12" cy="12" r="10"/>
          <path d="M12 2v20M2 12h20M12 2c-3 3-3 17 0 20M12 2c3 3 3 17 0 20" fill="none" stroke="#fff" stroke-width="1.2"/>
        </svg>
        <span>www.lumorapay.com</span>
      </li>
    </ul>

    <address class="address">
      48 Alder Ridge Way, Suite 210<br>
      Fairmont, CO 80115
    </address>
  </section>

  <section class="card card--back">
    <div class="wordmark">Lumora</div>
  </section>
</body>
</html>
```